business card design for a small scale specialty cut flower farm

We need a business card design for Hollowmere Bloom Farm based in Langley, BC, Canada. We produce specialty, high-end cut flowers and sell locally to florists, local shops and markets and the end user through bouquet subscriptions. The final business card design should be memorable and have a timeless or vintage feel. We would prefer a square shape.
Updates

Target Market(s)

florists, shops and seasonal markets, local flower lovers

Industry/Entity Type

Floral

Contact Information for Business Card

Tamsin Ellery Voss, Grower
Langley, BC, Canada
website: hollowmerebloomfarm.example
instagram: @hollowmerebloomfarm
Tel: 555.317.4290
facebook: www.facebook.example/hollowmereblooms/

Font styles to use
Serif
Decorative
Script

Requirements
Must have
• soft black background colour on front side, the included logo and catch phrase: Fresh Local Seasonal
Nice to have
• phone number and website address on front of card, included photo 6539 incorporated onto the back, possibly photo 6609 as well.

```html
<!DOCTYPE html>
<html lang="en">
<head>
<meta charset="utf-8">
<title>Hollowmere Bloom Farm – Business Card</title>
<link href="https://fonts.googleapis.com/css2?family=Didact+Gothic&family=Open+Sans:wght@400&display=swap" rel="stylesheet">
<style>
  :root {
    --page: #ffffff;
    --ink: #1a1a1a;
    --pink: #f08ce8;
    --petal-light: #f4d2f1;
    --petal: #e7a3e4;
    --leaf: #5f8f55;
    --card-edge: #8a8a8a;
  }
  html, body {
    margin: 0;
    padding: 0;
    width: 1200px;
    height: 1200px;
    overflow: hidden;
    background: var(--page);
  }
  .sheet {
    position: relative;
    width: 1200px;
    height: 1200px;
    font-family: "Didact Gothic", sans-serif;
    color: var(--ink);
  }
  .side-label {
    position: absolute;
    top: 164px;
    width: 456px;
    margin: 0;
    text-align: center;
    font-family: "Open Sans", sans-serif;
    font-weight: 400;
    font-size: 35px;
    letter-spacing: 1px;
  }
  .side-label--front { left: 90px; }
  .side-label--back { left: 640px; }

  .card {
    position: absolute;
    top: 276px;
    width: 456px;
    height: 456px;
    background: var(--page);
    border: 1px solid var(--card-edge);
    box-shadow: 4px 5px 6px rgba(0, 0, 0, 0.22);
    overflow: hidden;
    box-sizing: border-box;
  }
  .card--front { left: 100px; }
  .card--back { left: 640px; }

  .card__frame {
    position: absolute;
    top: 51px;
    left: 51px;
    width: 353px;
    height: 352px;
    border: 2px solid var(--ink);
    box-sizing: border-box;
  }

  /* Front */
  .brand {
    position: absolute;
    left: 0;
    width: 100%;
    text-align: center;
  }
  .brand__mark {
    position: absolute;
    top: 96px;
    left: 198px;
    width: 60px;
    height: 60px;
    border-radius: 50%;
    background: var(--pink);
  }
  .brand__name {
    top: 186px;
    font-size: 25px;
    letter-spacing: 2px;
    margin: 0;
    font-weight: 400;
    line-height: 1.15;
  }
  .brand__sub {
    top: 288px;
    font-size: 14px;
    margin: 0;
  }
  .brand__est {
    top: 316px;
    font-size: 10px;
    letter-spacing: 5px;
    margin: 0;
  }
  .tagline {
    position: absolute;
    top: 358px;
    left: 0;
    width: 100%;
    text-align: center;
    margin: 0;
    font-size: 21px;
    letter-spacing: 1px;
    color: var(--pink);
  }

  /* Back */
  .bloom-art {
    position: absolute;
    top: 0;
    left: 0;
    width: 98px;
    height: 410px;
    background: linear-gradient(180deg, var(--petal-light) 0%, var(--petal) 55%, var(--leaf) 100%);
  }
  .contact {
    position: absolute;
    left: 125px;
    width: 206px;
    text-align: center;
    margin: 0;
    white-space: nowrap;
  }
  .contact__name {
    top: 116px;
    font-size: 29px;
    line-height: 34px;
    font-weight: 400;
  }
  .contact__role {
    top: 184px;
    font-size: 18px;
    letter-spacing: 1.5px;
  }
  .contact__phone {
    top: 218px;
    left: 100px;
    width: 260px;
    font-size: 29px;
  }
  .social {
    position: absolute;
    top: 281px;
    left: 183px;
    display: flex;
    gap: 10px;
  }
  .social__dot {
    width: 40px;
    height: 40px;
    border-radius: 50%;
    background: var(--pink);
  }
  .contact__web {
    top: 330px;
    left: 80px;
    width: 296px;
    font-size: 16px;
    letter-spacing: 0.8px;
  }

  .print-note {
    position: absolute;
    top: 827px;
    left: 101px;
    width: 997px;
    height: 197px;
    border: 3px solid var(--ink);
    box-sizing: border-box;
    display: flex;
    align-items: center;
    justify-content: center;
    text-align: center;
    font-family: "Open Sans", sans-serif;
    font-size: 34px;
    line-height: 41px;
    letter-spacing: 0.5px;
    margin: 0;
  }
</style>
</head>
<body>
<main class="sheet">
  <h2 class="side-label side-label--front">SIDE 1</h2>
  <h2 class="side-label side-label--back">SIDE 2</h2>

  <section class="card card--front" aria-label="Card front">
    <div class="card__frame"></div>
    <span class="brand__mark" aria-hidden="true"></span>
    <h1 class="brand brand__name">HOLLOWMERE<br>BLOOM FARM</h1>
    <p class="brand brand__sub">Specialty Cut Flowers</p>
    <p class="brand brand__est">EST.2019</p>
    <p class="tagline">Fresh Local Seasonal</p>
  </section>

  <section class="card card--back" aria-label="Card back">
    <div class="card__frame"></div>
    <div class="bloom-art" role="img" aria-label="Watercolour wild rose blossom with a green leaf"></div>
    <h3 class="contact contact__name">Tamsin<br>Ellery Voss</h3>
    <p class="contact contact__role">OWNER</p>
    <p class="contact contact__phone">Tel (555) 317-4290</p>
    <div class="social" aria-label="Social media">
      <span class="social__dot"></span>
      <span class="social__dot"></span>
    </div>
    <p class="contact contact__web">hollowmerebloomfarm.example</p>
  </section>

  <p class="print-note">I would recommend a lightly textured paper stock<br>at least 400gsm (thickness)<br>This will give the vintage appearance sought after<br>&amp; further enhance the design</p>
</main>
</body>
</html>
```